Country Music Cruise Design

Current site
www.mapleharbors.com/index.php

We want a site that is Vibrant and Colorful with cartoon style graphics. This will be a bootstrap site and shall use that idea when designing.

We want a mixture of the two sites which we really like
http://www.ridgelinegetaway.com/
and
https://quilbymeet.net

Our logo is attached
Need a really nice one page design homepage with information and one page for the booking (www.mapleharbors.com/book)

country music fans on a cruise ship, 20-50 year old

4 page

Sans Serif

• Vibrant style colors and backgrounds like examples above.
• Dark color

```html
<!DOCTYPE html>
<html lang="en">
<head>
<meta charset="utf-8">
<title>Saltline Country Cruise</title>
<link rel="stylesheet" href="https://fonts.googleapis.com/css2?family=Bitter:wght@400;700&family=Open+Sans:wght@400;700&display=swap">
<style>
:root{
  --green:#1fa64a;
  --green-btn:#14a24a;
  --yellow:#f3de12;
  --gold:#efc20f;
  --orange:#f6a21c;
  --red:#d9332b;
  --brown:#8a2413;
  --footer:#3a3a3a;
  --ink:#111;
  --white:#fff;
  --muted:#bdbdbd;
}
*{box-sizing:border-box;margin:0;padding:0}
html,body{width:1200px;height:2808px;overflow:hidden}
body{position:relative;font-family:"Open Sans",Arial,sans-serif;color:var(--ink);background:var(--white)}
.section{position:absolute;left:0;width:1200px}

/* header */
.site-header{top:0;height:653px;background:linear-gradient(160deg,#3b4a5c 0%,#2d5f6e 40%,#4b6b7a 70%,#34404e 100%)}
.search{position:absolute;left:161px;top:37px;display:flex;height:38px}
.search-input{width:188px;background:var(--white);font-size:11px;color:#888;padding:12px 10px}
.search-btn{width:63px;background:var(--green-btn);display:flex;align-items:center;justify-content:center}
.social{position:absolute;right:161px;top:40px;display:flex;align-items:center;gap:10px;color:var(--white);font-size:11px;font-weight:700}
.social-icon{width:22px;height:22px;background:var(--white);border-radius:2px}
.brand{position:absolute;left:0;top:330px;width:1200px;text-align:center;font-family:"Bitter",Georgia,serif;font-weight:700;font-size:64px;color:var(--white);line-height:1}

/* nav */
.main-nav{top:653px;height:36px;background:var(--yellow);border-bottom:2px solid #d7c20c}
.nav-list{position:absolute;left:161px;top:0;height:36px;display:flex;align-items:center;list-style:none;font-size:12px;font-weight:700}
.nav-list li{display:flex;align-items:center}
.nav-list .sep{margin:0 40px}
.cart{position:absolute;left:979px;top:0;width:56px;height:36px;background:var(--red);display:flex;align-items:center;justify-content:center}

/* banner */
.banner{top:689px;height:706px;background:linear-gradient(180deg,#3aa6e0 0%,#9fd6f2 45%,#dff2fb 62%,#5cc3e3 72%,#bfe9f4 86%,#f6f1e2 100%)}
.banner-panel{position:absolute;left:253px;top:202px;width:696px;height:329px;background:rgba(240,250,245,.88);text-align:center}
.banner-title{font-family:"Bitter",Georgia,serif;font-weight:700;font-size:41px;margin-top:66px}
.banner-sub{font-size:16px;font-weight:700;margin-top:18px}
.btn-book{display:inline-block;margin-top:28px;width:176px;height:61px;line-height:61px;background:var(--green-btn);color:var(--white);font-size:17px;letter-spacing:.5px}

/* features */
.features{top:1395px;height:565px;background:var(--green)}
.feature{position:absolute;top:82px;width:330px;text-align:center;color:var(--white)}
.feature-photo{width:244px;height:244px;margin:0 auto;border-radius:50%;border:7px solid var(--white)}
.feature-title{font-family:"Bitter",Georgia,serif;font-weight:700;font-size:20px;margin-top:40px}
.feature-text{font-family:"Bitter",Georgia,serif;font-size:12px;line-height:21px;width:290px;margin:8px auto 0}
.btn-more{display:inline-block;margin-top:14px;width:120px;height:38px;line-height:38px;background:linear-gradient(#fbb832,var(--orange));border-radius:3px;font-size:9px;font-weight:700;color:var(--white)}

/* about */
.about{top:1960px;height:324px;background:var(--gold);text-align:center}
.about-title{font-family:"Bitter",Georgia,serif;font-weight:700;font-size:41px;margin-top:78px}
.about-text{font-family:"Bitter",Georgia,serif;font-size:13px;line-height:25px;width:810px;margin:22px auto 0;color:#4a3b00}

/* newsletter */
.newsletter{top:2284px;height:314px;background:var(--brown);text-align:center}
.newsletter-title{font-family:"Bitter",Georgia,serif;font-weight:700;font-size:41px;color:var(--white);margin-top:72px}
.newsletter-form{position:absolute;left:339px;top:163px;width:520px;height:67px;background:var(--white);display:flex;border-radius:3px}
.newsletter-icon{width:82px;display:flex;align-items:center;justify-content:center}
.newsletter-input{flex:1;background:var(--brown);margin:3px 0;text-align:left;padding-left:28px;font-size:10px;color:var(--white);line-height:61px}
.newsletter-btn{width:122px;line-height:67px;font-size:12px;font-weight:700}

/* footer */
.site-footer{top:2598px;height:210px;background:var(--footer);color:var(--muted);font-family:"Bitter",Georgia,serif;font-size:11px}
.footer-col{position:absolute;top:48px}
.footer-heading{font-family:"Open Sans",Arial,sans-serif;font-weight:700;font-size:11px;color:var(--white);margin-bottom:18px}
.footer-col ul{list-style:none}
.footer-col li{line-height:22px}
.contact-row{display:flex;align-items:center;gap:14px;line-height:30px}
.footer-social{position:absolute;left:902px;top:66px;display:flex;gap:10px}
.footer-social span{width:22px;height:22px;background:var(--white);border-radius:2px}
.copyright{position:absolute;right:161px;top:108px;text-align:right;line-height:20px}
</style>
</head>
<body>

<header class="section site-header" role="img" aria-label="Cartoon illustration of a cruise ship deck seen from above, with a pool, sun loungers and passengers">
  <div class="search">
    <div class="search-input">Search Here...</div>
    <div class="search-btn">
      <svg width="18" height="18" viewBox="0 0 18 18"><circle cx="7" cy="7" r="5" fill="none" stroke="#fff" stroke-width="2"/><line x1="11" y1="11" x2="16" y2="16" stroke="#fff" stroke-width="2.5"/></svg>
    </div>
  </div>
  <div class="social">Social Links :
    <span class="social-icon"></span><span class="social-icon"></span><span class="social-icon"></span><span class="social-icon"></span>
  </div>
  <div class="brand">Saltline Country Cruise</div>
</header>

<nav class="section main-nav">
  <ul class="nav-list">
    <li>PRICES</li><li class="sep">:</li>
    <li>WHAT'S INCLUDED?</li><li class="sep">:</li>
    <li>FAQ'S</li><li class="sep">:</li>
    <li>SHOP</li><li class="sep">:</li>
    <li>BOOK NOW</li>
  </ul>
  <div class="cart">
    <svg width="20" height="18" viewBox="0 0 20 18"><path d="M1 2h3l2 9h10l2-7H5" fill="none" stroke="#fff" stroke-width="2"/><circle cx="7" cy="15" r="1.6" fill="#fff"/><circle cx="15" cy="15" r="1.6" fill="#fff"/></svg>
  </div>
</nav>

<section class="section banner" role="img" aria-label="Cartoon tropical beach with palm trees, sunburst sky and a cruise ship on the sea">
  <div class="banner-panel">
    <h1 class="banner-title">SCC 2018 - JAN 12-15TH 2018</h1>
    <p class="banner-sub">DON'T BE LEFT ON SHORE!</p>
    <span class="btn-book">BOOK NOW</span>
  </div>
</section>

<section class="section features">
  <div class="feature" style="left:120px">
    <div class="feature-photo" role="img" aria-label="Photo of a cruise ship at sea seen from above" style="background:radial-gradient(circle,#e8eef2 0%,#3b6f93 45%,#123a5a 100%)"></div>
    <h2 class="feature-title">What's Included?</h2>
    <p class="feature-text">All SCC events, Food, Comedy Club, Kids Clubs, Game Shows, Night Clubs, GYM, Bars and Water Park</p>
    <span class="btn-more">LEARN MORE</span>
  </div>
  <div class="feature" style="left:435px">
    <div class="feature-photo" role="img" aria-label="Photo of guests dancing at an onboard party" style="background:radial-gradient(circle,#d9b08c 0%,#b8443a 45%,#5b7d96 100%)"></div>
    <h2 class="feature-title">SCC Activities</h2>
    <p class="feature-text">We will bring on bands, Southern California's favorite DJ's, Line Dance Lessons, Two Stepping, Contest, Offshore Parties</p>
    <span class="btn-more">LEARN MORE</span>
  </div>
  <div class="feature" style="left:749px">
    <div class="feature-photo" role="img" aria-label="Photo of performers on a lit stage" style="background:radial-gradient(circle,#e24a5a 0%,#7a2a6a 50%,#1a1a3a 100%)"></div>
    <h2 class="feature-title">Ship Itinerary</h2>
    <p class="feature-text">January 12th -15th<br>Friday - Leave Port 5:30 PM<br>Saturday - Ensenada Mexico - Formal</p>
    <span class="btn-more">LEARN MORE</span>
  </div>
</section>

<section class="section about">
  <h2 class="about-title">SCC 2018 - JAN 12-15TH 2018</h2>
  <p class="about-text">Country and Cruising? Don't miss out on this excursion that is 3 Nights – 2 Days on January 12th - 15th 2018 out of Long Beach. This cruise will be taken over by our West Coast Country family. We are putting boots onboard for two stepping, line dancing, multiple bands and our favorite Southern California Country DJ to bring it all together. Includes all food onboard, dance lessons, concerts, all ship activities and contest. DON'T WAIT! Rates will go up!</p>
</section>

<section class="section newsletter">
  <h2 class="newsletter-title">SUBSCRIBE TO OUR NEWSLETTER</h2>
  <div class="newsletter-form">
    <div class="newsletter-icon">
      <svg width="34" height="28" viewBox="0 0 34 28"><path d="M2 12 17 2l15 10v14H2z" fill="#333"/><path d="M6 10h22v9l-11 6-11-6z" fill="#fff"/><path d="M2 12l15 10 15-10" fill="none" stroke="#333" stroke-width="2"/></svg>
    </div>
    <div class="newsletter-input">ENTER YOUR E-AMIL</div>
    <div class="newsletter-btn">SUBSCRIBE</div>
  </div>
</section>

<footer class="section site-footer">
  <div class="footer-col" style="left:161px">
    <h3 class="footer-heading">CONTACT US</h3>
    <div class="contact-row">
      <svg width="14" height="14" viewBox="0 0 14 14"><path d="M3 1l3 3-2 2c1 2 2 3 4 4l2-2 3 3-2 2C6 13 1 8 1 3z" fill="#888"/></svg>1-800-555-0142
    </div>
    <div class="contact-row">
      <svg width="14" height="10" viewBox="0 0 14 10"><rect x="0.5" y="0.5" width="13" height="9" fill="none" stroke="#888"/><path d="M1 1l6 5 6-5" fill="none" stroke="#888"/></svg>info@mapleharbors.com
    </div>
  </div>
  <div class="footer-col" style="left:406px">
    <h3 class="footer-heading">QUICK LINKS</h3>
    <ul><li>Prices</li><li>Pics &amp; Vids</li><li>Press</li><li>FAQ's</li></ul>
  </div>
  <div class="footer-col" style="left:547px;top:84px">
    <ul><li>Vendors</li><li>Sponsors</li><li>About</li></ul>
  </div>
  <div class="footer-col" style="left:655px">
    <h3 class="footer-heading">KEY FEATURES</h3>
    <ul><li>Live Bands</li><li>Line Dancing</li><li>Contest</li><li>All you can drink packages</li></ul>
  </div>
  <div class="footer-social"><span></span><span></span><span></span><span></span></div>
  <p class="copyright">Copyright ©2018 Saltline Country Cruise<br>All Rights Reserved</p>
</footer>

</body>
</html>
```